Tarvimo Software (a new software house) needs a Wordpress web site

We need a Wordpress web site. We develop innovative software as a service (on demand) for companies and cunsumers.
Updates

Project Deadline Extended
Reason: I need extra days to analyze.

Target Market(s)

Consumers who use mobile software to access useful information about your day by day in a crowd plataform and on demand.

Industry/Entity Type

Software

Requirements
Must have
• See wordpress template suggestion:
http://themes.plondavi.com/?theme=marbleton

```html
<!DOCTYPE html>
<html lang="en">
<head>
<meta charset="utf-8">
<title>Tarvimo Software</title>
<link href="https://fonts.googleapis.com/css2?family=Oswald:wght@300;400&family=Roboto+Condensed:wght@300;400&display=swap" rel="stylesheet">
<style>
:root{
  --accent:#4a84c6;
  --accent-soft:#6b9bd3;
  --ink:#2f3237;
  --muted:#8a8d91;
  --header-bg:#f6f6f6;
  --page-bg:#eceef0;
  --panel:#ffffff;
  --hero-light:#47acdf;
  --hero-dark:#1a6aa3;
  --hero-sub:#1d3a57;
  --footer:#3b3c3f;
  --footer-stripe:#4a84c6;
  --caption:rgba(40,40,40,.72);
}
*{margin:0;padding:0;box-sizing:border-box}
html,body{width:1034px;height:1200px;overflow:hidden}
body{position:relative;background:var(--page-bg);font-family:'Roboto Condensed',sans-serif;color:var(--ink)}
.abs{position:absolute}

/* header */
.site-header{position:absolute;left:0;top:0;width:1034px;height:61px;background:linear-gradient(#fbfbfb,#eeeeee);border-bottom:1px solid #d8d8d8}
.brand{position:absolute;left:86px;top:17px;display:flex;align-items:center;gap:9px}
.brand-dot{width:24px;height:24px;border-radius:50%;background:var(--ink)}
.brand-name{font-family:'Oswald',sans-serif;font-weight:400;font-size:21px;color:var(--ink);letter-spacing:.3px}
.main-nav{position:absolute;left:412px;top:0;height:60px;display:flex}
.main-nav a{display:block;height:60px;line-height:54px;padding:0 20px;font-family:'Oswald',sans-serif;font-weight:300;font-size:15.5px;color:var(--ink);text-decoration:none;border-right:1px solid #dcdcdc}
.main-nav a:last-child{border-right:none}

/* hero */
.hero{position:absolute;left:0;top:61px;width:1034px;height:404px;background:radial-gradient(ellipse at 55% 40%,var(--hero-light),var(--hero-dark) 85%)}
.lang{position:absolute;left:828px;top:0;width:107px;height:34px;background:linear-gradient(#3c3d40,#1f2022);border-radius:0 0 6px 6px;color:#fff;font-family:'Oswald',sans-serif;font-weight:300;font-size:13px;display:flex;align-items:center;justify-content:center;gap:7px;box-shadow:0 2px 4px rgba(0,0,0,.35)}
.flag{width:22px;height:13px;background:#2d3f7c;border:1px solid #fff}
.hero-art{position:absolute;left:113px;top:77px;width:350px;height:325px;border-radius:6px;background:linear-gradient(160deg,#2a2b2e,#111214)}
.hero-art .screen{position:absolute;left:15px;top:18px;width:318px;height:165px;background:#f3f5f7}
.hero-title{position:absolute;left:519px;top:157px;width:405px;font-family:'Oswald',sans-serif;font-weight:300;color:#fff;font-size:31px;line-height:1.1;letter-spacing:-.4px;white-space:nowrap}
.hero-sub{position:absolute;left:519px;top:197px;width:400px;font-family:'Oswald',sans-serif;font-weight:300;color:var(--hero-sub);font-size:21.5px;line-height:1.35;letter-spacing:-.2px}
.hero-arrow{position:absolute;top:170px}

/* content panel */
.panel{position:absolute;left:73px;top:465px;width:888px;height:677px;background:var(--panel)}
.features{position:absolute;left:86px;top:465px;width:862px;height:181px;display:flex;background:linear-gradient(#fff,#f3f5f7)}
.feature{flex:1;text-align:center;padding-top:38px;border-right:1px solid #e6e6e6}
.feature:last-child{border-right:none}
.feature svg{display:block;margin:0 auto 12px}
.feature h3{font-family:'Oswald',sans-serif;font-weight:300;font-size:16.5px;color:var(--accent);margin-bottom:3px}
.feature p{font-weight:300;font-size:12.5px;line-height:16.5px;color:var(--muted);width:222px;margin:0 auto;text-align:justify;letter-spacing:-.2px}

.section-title{position:absolute;left:86px;display:flex;align-items:center;width:862px;font-family:'Oswald',sans-serif;font-weight:300;font-size:18.5px;color:var(--accent)}
.section-title::after{content:"";flex:1;margin-left:8px;border-bottom:1px dotted #c4c4c4;transform:translateY(3px)}

.shot{position:absolute;top:727px;height:126px;background:linear-gradient(#6c8f3a 0,#e9ece4 22%,#f4f4f2 60%,#c65b3e 78%,#7a9a3e 100%);border:1px solid #cfcfcf;overflow:hidden}
.shot .caption{position:absolute;left:0;right:0;top:88px;height:38px;background:var(--caption);color:#fff;font-weight:300;font-size:13.5px;line-height:16px;padding:2px 4px;white-space:nowrap;overflow:hidden}

.slider{position:absolute;left:86px;width:862px;height:14px}
.slider .line{position:absolute;left:14px;right:14px;top:7px;border-top:1px solid #777}
.slider .knob{position:absolute;left:30px;top:2px;width:10px;height:10px;border-radius:50%;background:var(--accent)}

.post{position:absolute;top:972px;width:420px}
.post .thumb{position:absolute;left:0;top:0;width:190px;height:114px;border:1px solid #c9c9c9;background:linear-gradient(#f4f6f8,#dfe6ea 55%,#f7f7f7)}
.post .body{position:absolute;left:200px;top:0;width:212px}
.post h4{font-family:'Oswald',sans-serif;font-weight:300;font-size:13.5px;color:var(--accent);line-height:16px;margin-top:1px;white-space:nowrap}
.post p{font-weight:300;font-size:12.5px;line-height:16.5px;color:var(--muted);text-align:justify;letter-spacing:-.2px}
.post time{display:block;font-family:'Oswald',sans-serif;font-weight:300;font-size:12px;color:var(--accent);margin-top:1px}

/* footer */
.site-footer{position:absolute;left:0;top:1142px;width:1034px;height:58px;background:var(--footer);border-top:4px solid var(--footer-stripe)}
.foot-nav{position:absolute;left:94px;top:13px;display:flex;gap:46px}
.foot-nav a{font-family:'Oswald',sans-serif;font-weight:300;font-size:15.5px;color:#fff;text-decoration:none}
.social{position:absolute;left:834px;top:16px;display:flex;gap:8px}
.social span{width:22px;height:22px;border-radius:50%;background:#fff;border:3px solid var(--accent)}
</style>
</head>
<body>

<header class="site-header">
  <div class="brand"><span class="brand-dot"></span><span class="brand-name">Tarvimo Software</span></div>
  <nav class="main-nav">
    <a href="#">Services</a><a href="#">Products</a><a href="#">Portfolio</a><a href="#">Blog</a><a href="#">Company</a><a href="#">Marketplace</a>
  </nav>
</header>

<section class="hero">
  <div class="lang">ENGLISH <span class="flag"></span>
    <svg width="10" height="8" viewBox="0 0 10 8"><path d="M0 0H10L5 8Z" fill="#fff"/></svg>
  </div>
  <div class="hero-art" role="img" aria-label="Desktop monitor, tablet and phone showing a web analytics dashboard"><div class="screen"></div></div>
  <svg class="hero-arrow" style="left:58px" width="28" height="74" viewBox="0 0 28 74"><path d="M24 2L6 37L24 72" fill="none" stroke="#fff" stroke-width="7"/></svg>
  <svg class="hero-arrow" style="left:948px" width="28" height="74" viewBox="0 0 28 74"><path d="M4 2L22 37L4 72" fill="none" stroke="#fff" stroke-width="7"/></svg>
  <h1 class="hero-title">WE DEVELOP INNOVATIVE SOFTWARE</h1>
  <p class="hero-sub">AS A SERVICE (ON DEMAND) FOR COMPANIES AND CUNSUMERS</p>
</section>

<div class="panel"></div>

<section class="features">
  <div class="feature">
    <svg width="26" height="30" viewBox="0 0 26 30"><path d="M13 1C6 1 2 6 2 12c0 3 1 5 3 7v10h10v-4h4c2 0 3-1 3-3v-4h3l-3-6C22 5 18 1 13 1Z" fill="#111"/><circle cx="13" cy="12" r="5" fill="none" stroke="#fff" stroke-width="2"/></svg>
    <h3>RESPONSIVE LAYOUT</h3>
    <p>Nulla tincidunt ultricies sodales. Pellentesque sed nisl mauris, sit amet sodales sem.</p>
  </div>
  <div class="feature">
    <svg width="28" height="34" viewBox="0 0 28 34"><rect x="3" y="0" width="24" height="34" rx="2" fill="#1a1a1a"/><rect x="0" y="4" width="5" height="2" fill="#555"/><rect x="0" y="10" width="5" height="2" fill="#555"/><rect x="0" y="16" width="5" height="2" fill="#555"/><rect x="0" y="22" width="5" height="2" fill="#555"/><rect x="0" y="28" width="5" height="2" fill="#555"/></svg>
    <h3>PORTFOLIO MODULE</h3>
    <p>Nulla tincidunt ultricies sodales. Pellentesque sed nisl mauris, sit amet sodales sem.</p>
  </div>
  <div class="feature">
    <svg width="28" height="28" viewBox="0 0 28 28"><circle cx="14" cy="14" r="12.5" fill="#111"/><path d="M6 8c3 0 5 2 4 5s-3 3-2 7l-2 1C4 16 4 11 6 8ZM16 5c3 1 6 3 6 6-2 0-4 2-3 4s-1 5-3 6c0-3-2-5-2-8s2-4 2-8Z" fill="#fff"/></svg>
    <h3>SUPPORT MULTI LANGUAGES</h3>
    <p>Nulla tincidunt ultricies sodales. Pellentesque sed nisl mauris, sit amet sodales sem.</p>
  </div>
</section>

<h2 class="section-title" style="top:668px">LATEST SOFTWARES</h2>

<div class="shot" style="left:86px;width:216px" role="img" aria-label="Screenshot of a recipe website with fresh vegetables"><div class="caption">Nulla tincidunt ultricies sodales. Pellen-<br>tesque sed nisl mauris.</div></div>
<div class="shot" style="left:326px;width:216px" role="img" aria-label="Screenshot of a recipe website with fresh vegetables"><div class="caption">Nulla tincidunt ultricies sodales. Pellen-<br>tesque sed nisl mauris.</div></div>
<div class="shot" style="left:570px;width:216px" role="img" aria-label="Screenshot of a recipe website with fresh vegetables"><div class="caption">Nulla tincidunt ultricies sodales. Pellen-<br>tesque sed nisl mauris.</div></div>
<div class="shot" style="left:805px;width:143px" role="img" aria-label="Screenshot of a recipe website with fresh vegetables"><div class="caption">Nulla tincidunt ultricies so<br>tesque sed nisl mauris.</div></div>

<div class="slider" style="top:871px">
  <svg class="abs" style="left:0;top:2px" width="8" height="10" viewBox="0 0 8 10"><path d="M7 0L1 5L7 10" fill="none" stroke="#111" stroke-width="2"/></svg>
  <div class="line"></div><div class="knob"></div>
  <svg class="abs" style="right:0;top:2px" width="8" height="10" viewBox="0 0 8 10"><path d="M1 0L7 5L1 10" fill="none" stroke="#111" stroke-width="2"/></svg>
</div>

<h2 class="section-title" style="top:926px">RECENT BLOG POST</h2>

<article class="post" style="left:91px">
  <div class="thumb" role="img" aria-label="Screenshot of a content management website"></div>
  <div class="body">
    <h4>AS A SERVICE (ON DEMAND) FOR COMPANIES</h4>
    <p>Nulla tincidunt ultricies sodales. Pellentesque sed nisl mauris, sit amet sodales sem.Nulla tincidunt ultricies sodales. Pellentesque sed nisl mauris, sit amet sodales sem.Nulla tincidunt ultricies sodales.</p>
    <time>JULY 12, 2013</time>
  </div>
</article>
<article class="post" style="left:527px">
  <div class="thumb" role="img" aria-label="Screenshot of a content management website"></div>
  <div class="body">
    <h4>AS A SERVICE (ON DEMAND) FOR COMPANIES</h4>
    <p>Nulla tincidunt ultricies sodales. Pellentesque sed nisl mauris, sit amet sodales sem.Nulla tincidunt ultricies sodales. Pellentesque sed nisl mauris, sit amet sodales sem.Nulla tincidunt ultricies sodales.</p>
    <time>JULY 12, 2013</time>
  </div>
</article>

<div class="slider" style="top:1102px">
  <svg class="abs" style="left:0;top:2px" width="8" height="10" viewBox="0 0 8 10"><path d="M7 0L1 5L7 10" fill="none" stroke="#111" stroke-width="2"/></svg>
  <div class="line"></div><div class="knob"></div>
  <svg class="abs" style="right:0;top:2px" width="8" height="10" viewBox="0 0 8 10"><path d="M1 0L7 5L1 10" fill="none" stroke="#111" stroke-width="2"/></svg>
</div>

<footer class="site-footer">
  <nav class="foot-nav">
    <a href="#">Services</a><a href="#">Products</a><a href="#">Portfolio</a><a href="#">Blog</a><a href="#">Company</a><a href="#">Marketplace</a>
  </nav>
  <div class="social"><span></span><span></span><span></span><span></span></div>
</footer>

</body>
</html>
```